2023 Wall Calendar Design - 11" x 8.5"

OVERVIEW:

The theme for this calendar is American (red-white-blue) and should have a modern feel. Please see website links and attached logos.

This calendar will feature screenshots and behind-the-scenes photos from all Harbor Lantern Shows found on our website.

We will supply screenshots for you to choose from via a Dropbox link once selected. Some sample screenshots are attached to get you started on design concepts.

SPECIFICATIONS:

28 PAGES – Cover, Back Cover, Inside Cover x 2, 24 calendar pages @ 2 pages / month

SIZE: 11” x 8.5” finished – excluding bleed

FULL COLOR – CMYK

See deliverables at bottom also.

DESIGN & THEME:

Each page will be 11" x 8.5" finished (excluding bleed margins) and have 2 pages for each month plus front and back cover and inside pages - total 28 pages. A sizing template is attached for your reference.

The pages will have a scoring hole for hanging on the wall.

The front cover will be a cover design that should make the calendar look appealing and reflect our brand and theme well.

Please see our websites listed below to get a feel for our branding.

INSIDE DESIGN INFO:

For the calendar date pages there will be a main photo on 1 page with a short photo description. On the dates page, the dates will be in squares so a person can write in them (IMPORTANT).

Relevant squares will also have special days in them including show premiere dates, US holidays, show stars birthdays, company anniversary, etc.

Some date pages may / can have mini photos on them as well. Some months have more than 1 photo that could be used if the design works for it.

We will supply special dates & holidays shortly but want to get started on the design style now while we complete assembly of the dates.

The inside cover pages (2) will have some info about our brand and maybe some photos that didn't make it into the main calendar pages.

The back cover can have a collage of all 12 main photos like they normally have with wall calendars that you buy on sites like Pagefold.example.

SOME CALENDAR LAYOUTS WE LIKE:
Not necessarily the STYLE/DESIGN but the LAYOUT for content only:

https://www.pagefold.example/shop/item-a-2023-wall-calendar/100000000001

https://www.pagefold.example/shop/item-b-2023-wall-calendar/100000000002

https://www.pagefold.example/shop/item-c-2023-wall-calendar/100000000003

https://www.pagefold.example/shop/item-d-2023-wall-calendar/100000000004

https://www.pagefold.example/shop/item-e-2023-wall-calendar/100000000005

https://www.pagefold.example/shop/item-f-2023-wall-calendar/100000000006

NOTE: I've also attached a mock-up of our 2022 calendar so you can see it.

DESIGN COLLATERAL:

We've attached our corporate logos, fonts, and some sample images that can be used in the calendar to start the layout concepts.

We will be compiling special dates and featured text while we review design concepts to select our winner.

Logo font - Stencil - https://typeshelf.example/fonts/stencil

Company sites: HarborLanternMedia.example | HarborLantern.example

Deliverables:

Full CMYK color, print ready PDF file formatted to 350 dpi – max file size 75 MB

Use attached template to finalize file sizes & bleeds

Fully editable layered AI source file (DO NOT USE COREL DRAW – we cannot read these files)

Fully editable In Design source file

Fully editable layered PSD source file (smart objects preferred)

Supply all fonts used so we may edit the calendar later – fonts must be licensed for your commercial use already or contact us to acquire any needed fonts.

We have licenses for all Adobe & Envato Elements fonts. Google & Microsoft fonts are also options. If you need us to acquire fonts from Envato or Adobe for your use, please let us know.

We have the Adobe Creative Suite. Any files you supply must be compatible with this software for both reading AND editing – including text.

If you have any questions, please feel free to message us and ask them.

Thank you & good luck!

Target Market(s)

American entertainment fans of TV

Industry/Entity Type

Television

Colors
0054AA
0677BA
7BADD7
CADEEF
E8F1F8
EB3D1F
EC4F4E
F09395
F8D3D4
FCEDEE

Requirements
Must have
• calendar as specified with writable date squares - see brief

```html
<!DOCTYPE html>
<html lang="en">
<head>
<meta charset="utf-8">
<title>Harbor Lantern Shows — January 2023 Calendar Page</title>
<link rel="stylesheet" href="https://fonts.googleapis.com/css2?family=Montserrat:ital,wght@0,400;0,600;0,800;1,400;1,600&family=Alfa+Slab+One&display=swap">
<style>
  :root {
    --navy: #2b3f7a;
    --navy-deep: #1f2f63;
    --red: #c8302f;
    --red-soft: #e25250;
    --blush: #f6ddd3;
    --blush-light: #fbf1ec;
    --paper: #ffffff;
    --backdrop: #f1f1f1;
    --ink: #2b3f7a;
    --photo-sky: #2f6fb0;
    --photo-night: #1c2d44;
    --photo-fire: #d9772f;
  }
  * { box-sizing: border-box; margin: 0; padding: 0; }
  html, body { width: 1200px; height: 900px; overflow: hidden; }
  body {
    background: var(--backdrop);
    font-family: "Montserrat", sans-serif;
    color: var(--ink);
    position: relative;
  }
  .calendar-page {
    position: absolute;
    left: 250px; top: 25px;
    width: 700px; height: 850px;
    background: linear-gradient(to bottom, var(--paper) 0, var(--paper) 640px, var(--blush) 830px);
    box-shadow: 0 6px 24px rgba(0,0,0,.12);
    overflow: hidden;
  }
  .feature-photo {
    position: absolute; left: 0; top: 0;
    width: 700px; height: 472px;
    background:
      radial-gradient(ellipse 120px 150px at 48% 72%, rgba(232,140,60,.95), rgba(217,119,47,.35) 60%, transparent 100%),
      linear-gradient(to bottom, var(--photo-sky) 0%, #3d78b3 28%, var(--photo-night) 62%, #3a2a22 100%);
  }
  .accent-band { position: absolute; left: 0; top: 462px; width: 700px; height: 34px; display: block; }
  .footer-band { position: absolute; left: 0; bottom: 0; width: 700px; height: 16px; display: block; }

  .brand-lockup {
    position: absolute; right: 28px; top: 520px;
    display: flex; align-items: center; gap: 12px;
  }
  .brand-mark { width: 22px; height: 22px; border-radius: 50%; background: var(--red); }
  .brand-name {
    font-family: "Montserrat", sans-serif;
    font-weight: 800; font-size: 30px; line-height: 1;
    color: var(--navy); letter-spacing: .5px;
  }
  .brand-site {
    position: absolute; right: 28px; top: 560px;
    font-size: 12px; font-weight: 600; color: var(--navy);
  }

  .month-title {
    position: absolute; left: 56px; top: 592px;
    font-weight: 800; font-size: 28px; letter-spacing: 2px; color: var(--navy);
  }

  .date-grid {
    position: absolute; left: 28px; top: 640px;
    width: 400px;
  }
  .weekdays, .days { display: grid; grid-template-columns: repeat(7, 52px); column-gap: 6px; }
  .weekdays span {
    font-size: 8px; font-style: italic; text-align: center;
    text-transform: uppercase; color: var(--navy);
  }
  .weekdays .weekend { color: var(--red); }
  .days { row-gap: 5px; margin-top: 5px; }
  .day {
    height: 30px; border: 1px solid var(--navy);
    background: var(--paper);
    position: relative;
  }
  .day span {
    position: absolute; right: 3px; bottom: 1px;
    font-size: 10px; font-style: italic; color: var(--navy);
  }
  .day.weekend span { color: var(--red); }
  .day.next-month { opacity: .25; background: transparent; }

  .year-title {
    position: absolute; right: 28px; top: 596px;
    font-family: "Alfa Slab One", serif;
    font-size: 62px; line-height: 1; color: var(--red);
    font-style: normal; letter-spacing: 2px;
  }
  .photo-caption {
    position: absolute; right: 28px; top: 680px; width: 230px;
    font-size: 8.5px; font-style: italic; line-height: 1.45; color: var(--navy);
  }
  .photo-caption p + p { margin-top: 10px; }
</style>
</head>
<body>
  <article class="calendar-page">
    <div class="feature-photo" role="img" aria-label="Photo: friends gathered around a campfire at dusk in the mountains, beside a tent"></div>

    <svg class="accent-band" viewBox="0 0 700 34" preserveAspectRatio="none" aria-hidden="true">
      <rect x="0" y="10" width="700" height="24" fill="#2b3f7a"/>
      <polygon points="0,10 700,0 700,12 0,22" fill="#2b3f7a"/>
      <polygon points="90,22 150,21 130,34 70,34" fill="#c8302f"/>
      <polygon points="160,20 175,20 155,34 140,34" fill="#c8302f"/>
      <polygon points="600,2 660,1 640,14 580,15" fill="#c8302f"/>
      <polygon points="670,1 700,0 700,12 650,13" fill="#c8302f"/>
      <rect x="0" y="0" width="700" height="0" fill="none"/>
    </svg>

    <div class="brand-lockup">
      <span class="brand-mark"></span>
      <span class="brand-name">Harbor Lantern Shows</span>
    </div>
    <div class="brand-site">HarborLantern.example</div>

    <h1 class="month-title">JANUARY</h1>

    <section class="date-grid" aria-label="January 2023 dates">
      <div class="weekdays">
        <span class="weekend">Sunday</span><span>Monday</span><span>Tuesday</span><span>Wednesday</span><span>Thursday</span><span>Friday</span><span class="weekend">Saturday</span>
      </div>
      <div class="days">
        <div class="day weekend"><span>1</span></div><div class="day"><span>2</span></div><div class="day"><span>3</span></div><div class="day"><span>4</span></div><div class="day"><span>5</span></div><div class="day"><span>6</span></div><div class="day weekend"><span>7</span></div>
        <div class="day weekend"><span>8</span></div><div class="day"><span>9</span></div><div class="day"><span>10</span></div><div class="day"><span>11</span></div><div class="day"><span>12</span></div><div class="day"><span>13</span></div><div class="day weekend"><span>14</span></div>
        <div class="day weekend"><span>15</span></div><div class="day"><span>16</span></div><div class="day"><span>17</span></div><div class="day"><span>18</span></div><div class="day"><span>19</span></div><div class="day"><span>20</span></div><div class="day weekend"><span>21</span></div>
        <div class="day weekend"><span>22</span></div><div class="day"><span>23</span></div><div class="day"><span>24</span></div><div class="day"><span>25</span></div><div class="day"><span>26</span></div><div class="day"><span>27</span></div><div class="day weekend"><span>28</span></div>
        <div class="day weekend"><span>29</span></div><div class="day"><span>30</span></div><div class="day"><span>31</span></div><div class="day next-month"><span>1</span></div><div class="day next-month"><span>2</span></div><div class="day next-month"><span>3</span></div><div class="day next-month"><span>4</span></div>
        <div class="day next-month"><span>5</span></div><div class="day next-month"><span>6</span></div><div class="day next-month"><span>7</span></div><div class="day next-month"><span>8</span></div><div class="day next-month"><span>9</span></div><div class="day next-month"><span>10</span></div><div class="day next-month"><span>11</span></div>
      </div>
    </section>

    <div class="year-title">2023</div>

    <div class="photo-caption">
      <p>Gathered around a mountain campfire as the last light fades, the crew trades stories from a long season on the road. Every ember marks a scene we still talk about, a line that landed, a shot we almost missed.</p>
      <p>Behind the camera, January begins with cold hands and warm coffee. Our first shoot of the year started here, under a sky that turned from blue to black in minutes.</p>
    </div>

    <svg class="footer-band" viewBox="0 0 700 16" preserveAspectRatio="none" aria-hidden="true">
      <rect x="0" y="0" width="700" height="16" fill="#2b3f7a"/>
      <polygon points="60,0 150,0 140,16 50,16" fill="#c8302f"/>
      <polygon points="165,0 180,0 170,16 155,16" fill="#c8302f"/>
      <polygon points="560,0 650,0 640,16 550,16" fill="#c8302f"/>
    </svg>
  </article>
</body>
</html>
```